Construction company stationary design

We're wanting to develop a new professional stationary set for a newly establised property related business using our existing logo (attached). Business incorporates renovations, property investment and property development.

Specifically needing letter head, business cards, envelopes, email signature and need to get tshirt and caps embroydered.

Looking for something quite modern but professional using white, black and green.

Investment

```html
<!DOCTYPE html>
<html lang="en">
<head>
<meta charset="utf-8">
<title>Kestrel Build – Business Card</title>
<link href="https://fonts.googleapis.com/css2?family=Mulish:wght@400;700;800&display=swap" rel="stylesheet">
<style>
  :root {
    --backdrop: #5b5b5b;
    --paper: #f7f7f5;
    --green: #78b82a;
    --green-dark: #4e8a1b;
    --ink: #6b6b6b;
    --ink-strong: #555555;
    --white: #ffffff;
  }
  * { margin: 0; padding: 0; box-sizing: border-box; }
  html, body {
    width: 1200px; height: 1000px; overflow: hidden;
    background: var(--backdrop);
    font-family: "Mulish", sans-serif;
  }
  .canvas { position: relative; width: 1200px; height: 1000px; }

  .card {
    position: absolute;
    width: 528px; height: 300px;
    border-radius: 14px;
    overflow: hidden;
  }
  .card-front { left: 207px; top: 165px; background: var(--paper); }
  .card-back {
    left: 473px; top: 551px;
    background: linear-gradient(135deg, var(--green) 0%, #67a624 55%, var(--green-dark) 100%);
  }

  .wordmark {
    position: absolute;
    font-weight: 800;
    letter-spacing: 0.5px;
    line-height: 1;
    text-transform: uppercase;
  }
  .card-front .wordmark { left: 88px; top: 96px; width: 178px; font-size: 33px; color: var(--green); text-align: center; }
  .card-back .wordmark { left: 45px; top: 78px; width: 176px; font-size: 33px; color: var(--white); text-align: center; }

  .address {
    position: absolute; right: 262px; top: 207px;
    font-size: 12.5px; line-height: 16px; color: var(--ink);
    text-align: right;
  }
  .divider {
    position: absolute; left: 307px; top: 208px;
    width: 1px; height: 32px; background: #8a8a8a;
  }

  .contact { position: absolute; left: 349px; color: var(--ink); font-size: 12.5px; line-height: 16px; }
  .contact b { color: var(--ink-strong); font-weight: 700; }
  .person { top: 98px; }
  .person-name { font-size: 15px; font-weight: 800; color: var(--green); letter-spacing: 0.6px; line-height: 20px; }
  .person-title { margin-top: 2px; font-size: 13px; }
  .phones { top: 162px; }
  .online { top: 207px; }

  .accent-bar {
    position: absolute; left: 308px; bottom: 0;
    width: 220px; height: 14px; background: var(--green);
  }

  .web {
    position: absolute; left: 55px; top: 246px;
    font-size: 15px; color: var(--white); letter-spacing: 0.4px;
  }
  .web b { font-weight: 800; }
</style>
</head>
<body>
<main class="canvas">
  <section class="card card-front" aria-label="Business card front">
    <div class="wordmark">Kestrel<br>Build</div>
    <p class="address">418 Ridgeway Ct. Suite 210<br>Boulder Falls, CO 80412</p>
    <span class="divider"></span>
    <div class="contact person">
      <p class="person-name">JORDAN ELLERY</p>
      <p class="person-title">Chief Manager</p>
    </div>
    <div class="contact phones">
      <p><b>Phone:</b> (555) 318-7020</p>
      <p><b>Fax:</b> (555) 318-7020</p>
    </div>
    <div class="contact online">
      <p><b>Email:</b> hello@kestrelbuild.com</p>
      <p><b>Web:</b> www.kestrelbuild.com</p>
    </div>
    <span class="accent-bar"></span>
  </section>

  <section class="card card-back" aria-label="Business card back">
    <div class="wordmark">Kestrel<br>Build</div>
    <p class="web">www.<b>kestrelbuild</b>.com</p>
  </section>
</main>
</body>
</html>
```